Bref créative
RON TALIVERO STATIONARY PACKAGE
Letterhead paper, Envelopes, Business Cards, Patient brochures, Flyer,Gift Certificate, T-Shirts
Professional
RON TALIVERO DDS
General & Cosmetic Dentistry
47-30 91 Street
Elmhurst, NY 11208
brightcuspdental@mailbox-example.com
www.brightcuspdental-example.com
I would like to present a very professional image for my company.
Smile!

```html
<!DOCTYPE html>
<html lang="en">
<head>
<meta charset="utf-8">
<title>Brightcusp Dental – Gift Certificates</title>
<link href="https://fonts.googleapis.com/css2?family=Almendra:ital,wght@0,700;1,700&family=Lora:ital@1&family=Open+Sans:wght@400;600&display=swap" rel="stylesheet">
<style>
  :root{
    --bg:#e9e6e2;
    --paper:#ffffff;
    --paper-edge:#f1f1ef;
    --ink:#2a2a2a;
    --muted:#6d6d6d;
    --rule:#c9c9c9;
    --green:#3d9a2c;
    --green-light:#8cc63f;
    --gold:#c9a227;
    --gold-light:#f0d66a;
    --black:#111111;
  }
  *{box-sizing:border-box;margin:0;padding:0}
  html,body{width:1200px;height:862px;overflow:hidden;background:var(--bg)}
  .sheet{position:relative;width:1200px;height:862px}
  .certificate{
    position:absolute;width:528px;height:212px;
    background:linear-gradient(180deg,var(--paper) 0%,var(--paper-edge) 100%);
    box-shadow:0 3px 8px rgba(0,0,0,.25);
    font-family:"Open Sans",sans-serif;color:var(--ink);overflow:hidden;
  }
  .col-left{left:38px}.col-right{left:622px}
  .row-1{top:62px}.row-2{top:326px}.row-3{top:590px}

  .brand-panel{position:absolute;left:0;top:0;width:160px;height:196px;border-right:1px solid var(--rule);padding:22px 0 0 22px}
  .brand{display:flex;align-items:center;gap:6px;margin-bottom:46px}
  .brand-dot{width:14px;height:14px;border-radius:50%;background:var(--green)}
  .brand-name{font-size:12px;font-weight:600;color:var(--green)}
  .contact{font-size:6px;line-height:9px;color:var(--muted)}
  .contact p:nth-child(3){margin-top:5px}

  .form{position:absolute;left:176px;top:14px;right:22px}
  .title{font-family:"Almendra",serif;font-weight:700;font-size:17px;text-align:center;margin-bottom:10px;padding-right:40px}
  .field{display:flex;align-items:flex-end;height:22px;font-family:"Lora",serif;font-style:italic;font-size:9px}
  .field .label{width:40px}
  .field .line{flex:1;border-bottom:1px solid var(--rule);height:1px;margin-bottom:3px}
  .sign-row{display:flex;gap:18px;margin-top:30px;font-family:"Lora",serif;font-style:italic;font-size:9px}
  .sign-row .part{flex:1;display:flex;flex-direction:column}
  .sign-row .part span{border-top:1px solid var(--rule);padding-top:2px}
  .sign-row .part:first-child{flex:1.6}

  .band{position:absolute;left:0;right:0;bottom:0;height:16px;display:flex;align-items:center;padding-left:14px}
  .band .web{font-size:6px;letter-spacing:.4px;color:#fff}
  .band-light{background:#f4f4f2;border-top:1px solid var(--rule)}
  .band-light .web{color:var(--muted)}
  .band-split{background:linear-gradient(90deg,var(--black) 0 52%,var(--green) 52% 70%,var(--gold) 70% 100%)}
  .band-black{background:var(--black)}
  .band-green{background:linear-gradient(90deg,#1f6b1a,var(--green) 40%,var(--green-light) 75%,#1f6b1a)}
  .band-black-accent{background:var(--black);border-top:3px solid var(--green)}
  .band-gold{background:linear-gradient(90deg,#8a6b10,var(--gold) 35%,var(--gold-light) 65%,var(--gold))}
  .band-gold .web{color:#3a2c00}
</style>
</head>
<body>
<main class="sheet">

  <section class="certificate col-left row-1">
    <div class="brand-panel">
      <div class="brand"><span class="brand-dot"></span><span class="brand-name">brightcuspdental</span></div>
      <div class="contact"><p>47-30 91 Street</p><p>Elmhurst, NY 11208</p><p>T (718) 555-0142</p><p>F (718) 555-0143</p><p>brightcuspdental@mailbox-example.com</p></div>
    </div>
    <div class="form">
      <h2 class="title">Gift Certificate</h2>
      <div class="field"><span class="label">To</span><span class="line"></span></div>
      <div class="field"><span class="label">For</span><span class="line"></span></div>
      <div class="field"><span class="label">From</span><span class="line"></span></div>
      <div class="sign-row"><div class="part"><span>Signature</span></div><div class="part"><span>Date</span></div></div>
    </div>
    <div class="band band-light"><span class="web">www.brightcuspdental-example.com</span></div>
  </section>

  <section class="certificate col-right row-1">
    <div class="brand-panel">
      <div class="brand"><span class="brand-dot"></span><span class="brand-name">brightcuspdental</span></div>
      <div class="contact"><p>47-30 91 Street</p><p>Elmhurst, NY 11208</p><p>T (718) 555-0142</p><p>F (718) 555-0143</p><p>brightcuspdental@mailbox-example.com</p></div>
    </div>
    <div class="form">
      <h2 class="title">Gift Certificate</h2>
      <div class="field"><span class="label">To</span><span class="line"></span></div>
      <div class="field"><span class="label">For</span><span class="line"></span></div>
      <div class="field"><span class="label">From</span><span class="line"></span></div>
      <div class="sign-row"><div class="part"><span>Signature</span></div><div class="part"><span>Date</span></div></div>
    </div>
    <div class="band band-split"><span class="web">www.brightcuspdental-example.com</span></div>
  </section>

  <section class="certificate col-left row-2">
    <div class="brand-panel">
      <div class="brand"><span class="brand-dot"></span><span class="brand-name">brightcuspdental</span></div>
      <div class="contact"><p>47-30 91 Street</p><p>Elmhurst, NY 11208</p><p>T (718) 555-0142</p><p>F (718) 555-0143</p><p>brightcuspdental@mailbox-example.com</p></div>
    </div>
    <div class="form">
      <h2 class="title">Gift Certificate</h2>
      <div class="field"><span class="label">To</span><span class="line"></span></div>
      <div class="field"><span class="label">For</span><span class="line"></span></div>
      <div class="field"><span class="label">From</span><span class="line"></span></div>
      <div class="sign-row"><div class="part"><span>Signature</span></div><div class="part"><span>Date</span></div></div>
    </div>
    <div class="band band-black"><span class="web">www.brightcuspdental-example.com</span></div>
  </section>

  <section class="certificate col-right row-2">
    <div class="brand-panel">
      <div class="brand"><span class="brand-dot"></span><span class="brand-name">brightcuspdental</span></div>
      <div class="contact"><p>47-30 91 Street</p><p>Elmhurst, NY 11208</p><p>T (718) 555-0142</p><p>F (718) 555-0143</p><p>brightcuspdental@mailbox-example.com</p></div>
    </div>
    <div class="form">
      <h2 class="title">Gift Certificate</h2>
      <div class="field"><span class="label">To</span><span class="line"></span></div>
      <div class="field"><span class="label">For</span><span class="line"></span></div>
      <div class="field"><span class="label">From</span><span class="line"></span></div>
      <div class="sign-row"><div class="part"><span>Signature</span></div><div class="part"><span>Date</span></div></div>
    </div>
    <div class="band band-green"><span class="web">www.brightcuspdental-example.com</span></div>
  </section>

  <section class="certificate col-left row-3">
    <div class="brand-panel">
      <div class="brand"><span class="brand-dot"></span><span class="brand-name">brightcuspdental</span></div>
      <div class="contact"><p>47-30 91 Street</p><p>Elmhurst, NY 11208</p><p>T (718) 555-0142</p><p>F (718) 555-0143</p><p>brightcuspdental@mailbox-example.com</p></div>
    </div>
    <div class="form">
      <h2 class="title">Gift Certificate</h2>
      <div class="field"><span class="label">To</span><span class="line"></span></div>
      <div class="field"><span class="label">For</span><span class="line"></span></div>
      <div class="field"><span class="label">From</span><span class="line"></span></div>
      <div class="sign-row"><div class="part"><span>Signature</span></div><div class="part"><span>Date</span></div></div>
    </div>
    <div class="band band-black-accent"><span class="web">www.brightcuspdental-example.com</span></div>
  </section>

  <section class="certificate col-right row-3">
    <div class="brand-panel">
      <div class="brand"><span class="brand-dot"></span><span class="brand-name">brightcuspdental</span></div>
      <div class="contact"><p>47-30 91 Street</p><p>Elmhurst, NY 11208</p><p>T (718) 555-0142</p><p>F (718) 555-0143</p><p>brightcuspdental@mailbox-example.com</p></div>
    </div>
    <div class="form">
      <h2 class="title">Gift Certificate</h2>
      <div class="field"><span class="label">To</span><span class="line"></span></div>
      <div class="field"><span class="label">For</span><span class="line"></span></div>
      <div class="field"><span class="label">From</span><span class="line"></span></div>
      <div class="sign-row"><div class="part"><span>Signature</span></div><div class="part"><span>Date</span></div></div>
    </div>
    <div class="band band-gold"><span class="web">www.brightcuspdental-example.com</span></div>
  </section>

</main>
</body>
</html>
```